Volren Goods Ltd Stationery Design Project

hi we need to design business cards, letter head, complimentary slips, scribble pads, note pads, envelopes for volren goods ltd.

please see business cards details

Kelvin Obutu

P.O Box 41873 -00312 Nairobi - Kenya
Tel: +254-733-218-904
Email: volrengoods@mailvexo.com

company name should appear on all stationery : Volren Goods Ltd

Industry/Entity Type

Business

Requirements
Must have
• kindly stick to colours in the logo

```html
<!DOCTYPE html>
<html lang="en">
<head>
<meta charset="utf-8">
<title>Volren Goods Ltd – Scribble Pad</title>
<link rel="stylesheet" href="https://fonts.googleapis.com/css2?family=Open+Sans:wght@400;600;700&display=swap">
<style>
  :root {
    --brand-orange: #f7a520;
    --brand-navy: #2b3990;
    --ink-grey: #8a8a8a;
    --rule-grey: #c8c8c8;
    --rule-dark: #4a4a4a;
    --motif-grey: #ececec;
    --paper: #ffffff;
  }
  html, body {
    margin: 0;
    padding: 0;
    width: 800px;
    height: 1200px;
    overflow: hidden;
    background: var(--paper);
  }
  .pad {
    position: relative;
    width: 800px;
    height: 1200px;
    overflow: hidden;
    background: var(--paper);
    font-family: "Open Sans", Verdana, sans-serif;
  }
  .corner-motif {
    position: absolute;
    left: 180px;
    top: 720px;
    width: 620px;
    height: 480px;
    background: radial-gradient(ellipse at 70% 65%, var(--motif-grey) 0%, rgba(236,236,236,0.55) 45%, rgba(255,255,255,0) 75%);
  }
  .brand-name {
    position: absolute;
    left: 430px;
    top: 28px;
    display: flex;
    align-items: center;
    gap: 6px;
    font-size: 17px;
    font-weight: 700;
    line-height: 1.05;
    color: var(--brand-orange);
    letter-spacing: 0.5px;
    text-align: center;
  }
  .brand-dot {
    width: 10px;
    height: 10px;
    border-radius: 50%;
    background: var(--brand-orange);
    flex: none;
  }
  .header-divider {
    position: absolute;
    left: 558px;
    top: 11px;
    width: 2px;
    height: 69px;
    background: var(--brand-navy);
  }
  .contact {
    position: absolute;
    left: 568px;
    top: 10px;
    margin: 0;
    color: var(--ink-grey);
    font-size: 10px;
    font-weight: 700;
    line-height: 13px;
  }
  .contact .company {
    color: var(--brand-navy);
    font-size: 13px;
    font-weight: 600;
    line-height: 18px;
    display: block;
    margin-bottom: 2px;
  }
  .contact .label { color: var(--brand-navy); }
  .desk-line {
    position: absolute;
    left: 27px;
    right: 17px;
    top: 123px;
    display: flex;
    justify-content: space-between;
    font-size: 9.5px;
    font-weight: 700;
    color: var(--brand-navy);
  }
  .date-field {
    display: flex;
    align-items: flex-end;
    gap: 3px;
  }
  .date-blank {
    width: 102px;
    border-bottom: 1px solid var(--brand-navy);
    height: 11px;
  }
  .header-rule {
    position: absolute;
    left: 0;
    right: 0;
    top: 138px;
    height: 4px;
    border-top: 1.5px solid var(--rule-dark);
    border-bottom: 1px solid var(--rule-dark);
  }
  .writing-lines {
    position: absolute;
    left: 0;
    right: 0;
    top: 147px;
    height: 978px;
    background: repeating-linear-gradient(to bottom, transparent 0, transparent 36.5px, var(--rule-grey) 36.5px, var(--rule-grey) 37.6px);
  }
</style>
</head>
<body>
  <main class="pad">
    <div class="corner-motif" role="img" aria-label="Faint brand motif in the lower right corner"></div>

    <header>
      <div class="brand-name"><span class="brand-dot"></span><span>VOLREN<br>GOODS</span></div>
      <div class="header-divider"></div>
      <p class="contact">
        <span class="company">Volren Goods Ltd</span>
        P.O Box 41873 -00312 Nairobi - Kenya<br>
        <span class="label">t:</span>&nbsp; +254-733-218-904<br>
        <span class="label">e:</span>&nbsp;volrengoods@mailvexo.com<br>
        <span class="label">w:</span>&nbsp;www.volrengoodsltd.com
      </p>
    </header>

    <div class="desk-line">
      <span>From the desk of</span>
      <span class="date-field">Date: <span class="date-blank"></span></span>
    </div>
    <div class="header-rule"></div>

    <div class="writing-lines"></div>
  </main>
</body>
</html>
```